Olive oil bottle labels, front and back.

Sophisticated uncluttered distinctive eye catching label
Front label:
Label on front like the uploaded file in design but called “Corrowick Hollow”, (not Marrabel Reach.)
Need to state that it’s extra virgin, cold pressed olive oil, 100% organic, grown and pressed on the Kellaway Peninsula.
500 ml
Back label:
Nutritional information table (see label example in uploaded files) including FFA 0.1% Oleic Acid
Storage: airtight in cool dark place
Made and produced in Australia from 100% Australian ingredients,
Harvest date:
Best by:
Batch:
Grown, harvested and bottled at The Hollow, Pellandry Rd. Tallowmere. 3847
The back label on uploaded files has the info requited except they should have address and don't include those industry and Australian made logos.
The front label is what we want, first to plagiarise without copyright infringement gets the gig, thanks.
Labels front and back need be 5 x 13 cm
Gourmet, up-market
- Love "Adorn Regular Garland"

```html
<!DOCTYPE html>
<html lang="en">
<head>
<meta charset="utf-8">
<title>Corrowick Hollow Extra Virgin Olive Oil – Front and Back Labels</title>
<link rel="stylesheet" href="https://fonts.googleapis.com/css2?family=Cinzel:wght@400;500&family=Pinyon+Script&family=Roboto+Condensed:wght@400;700&display=swap">
<style>
  :root {
    --page: #eeeeec;
    --label-light: #4a4a4b;
    --label-dark: #232324;
    --ink: #ecebe8;
    --ink-soft: #cfcfcf;
    --gold: #c9a54f;
    --gold-deep: #8a6a22;
    --gold-light: #f0d68a;
    --olive-light: #b8c94a;
    --olive-deep: #55701c;
    --note-bg: #e6e6e6;
    --note-ink: #333333;
  }
  * { box-sizing: border-box; margin: 0; padding: 0; }
  html, body {
    width: 1200px; height: 1200px; overflow: hidden;
    background: var(--page);
  }
  .canvas { position: relative; width: 1200px; height: 1200px; }

  /* Labels are built at 324 × 837 units (5 × 13 cm) and scaled up */
  .label {
    position: absolute; top: 83px;
    width: 324px; height: 837px;
    transform-origin: top left;
    transform: scale(1.235);
    background: linear-gradient(100deg, var(--label-light) 0%, #353536 35%, var(--label-dark) 100%);
    color: var(--ink);
    overflow: hidden;
  }
  .label--front { left: 160px; }
  .label--back { left: 640px; }
  .abs { position: absolute; }

  /* ---------- Front ---------- */
  .brand-vertical {
    left: 48px; top: 36px; height: 520px; width: 44px;
    writing-mode: vertical-rl; transform: rotate(180deg);
    font-family: "Cinzel", serif; font-size: 31px; letter-spacing: 7px;
    text-align: center; color: var(--ink); white-space: nowrap;
  }
  .pour-line {
    left: 71px; top: 558px; width: 2px; height: 196px;
    background: linear-gradient(var(--gold-light), var(--gold));
  }
  .pour-drop { left: 54px; top: 738px; }
  .brand-circle {
    left: 208px; top: 35px; width: 70px; height: 70px; border-radius: 50%;
    background: #1c1c1c; border: 3px solid var(--gold);
  }
  .olive-art {
    left: 121px; top: 107px; width: 187px; height: 122px; border-radius: 50% 40% 45% 55%;
    background: radial-gradient(ellipse at 55% 65%, var(--olive-light) 0%, #7f9a2c 45%, var(--olive-deep) 75%, transparent 78%);
  }
  .front-type { right: 28px; text-align: right; font-family: "Cinzel", serif; }
  .extra-virgin { top: 304px; font-size: 22px; line-height: 30px; letter-spacing: 1px; }
  .cold-pressed {
    right: 20px; top: 376px; width: 156px; padding: 4px 0 3px;
    border-top: 2px solid var(--gold); border-bottom: 2px solid var(--gold);
    font-size: 19px; text-align: center; letter-spacing: 0.5px;
  }
  .olive-oil {
    top: 428px; font-size: 44px; line-height: 44px;
    background: linear-gradient(180deg, var(--gold-deep) 0%, var(--gold) 45%, var(--gold-light) 100%);
    -webkit-background-clip: text; background-clip: text; color: transparent;
  }
  .organic {
    right: 28px; top: 628px; text-align: right;
    font-family: "Pinyon Script", cursive; font-size: 26px; line-height: 26px; color: var(--ink);
  }
  .organic-rule { right: 32px; top: 694px; width: 64px; height: 2px; background: var(--gold); }
  .volume { top: 710px; font-size: 18px; color: var(--gold); letter-spacing: 1px; }
  .origin { top: 754px; font-size: 11.5px; line-height: 16px; color: var(--ink-soft); letter-spacing: 0.5px; }

  /* ---------- Back ---------- */
  .back-circle {
    left: 124px; top: 27px; width: 66px; height: 66px; border-radius: 50%;
    background: #1c1c1c; border: 3px solid var(--gold);
  }
  .back-brand {
    left: 0; right: 0; top: 108px; text-align: center;
    font-family: "Cinzel", serif; font-size: 19px; letter-spacing: 3px; color: var(--ink);
  }
  .nutrition {
    left: 22px; top: 163px; width: 280px; height: 306px;
    border: 2px solid var(--ink); padding: 10px 10px 0;
    font-family: "Roboto Condensed", sans-serif; font-size: 10.5px; line-height: 16.4px;
    color: var(--ink);
  }
  .nutrition h2 { font-size: 21px; font-weight: 700; line-height: 26px; margin-bottom: 10px; letter-spacing: 0.3px; }
  .nutrition table { width: 100%; border-collapse: collapse; }
  .nutrition td { padding: 0; vertical-align: top; }
  .nutrition td:nth-child(2) { width: 74px; }
  .nutrition td:nth-child(3) { width: 38px; }
  .nutrition .head td { padding-bottom: 16px; }
  .nutrition .strong { font-weight: 700; }
  .nutrition .sub td:first-child { padding-left: 6px; }
  .back-text {
    left: 12px; right: 12px; text-align: center;
    font-family: "Roboto Condensed", sans-serif; font-weight: 700;
    font-size: 13px; line-height: 19px; letter-spacing: 0.3px;
  }
  .ingredients { top: 482px; }
  .storage { top: 542px; }
  .rule { left: 38px; width: 248px; height: 2px; background: var(--ink); }
  .rule--one { top: 572px; }
  .made { top: 582px; letter-spacing: 1.3px; }
  .rule--two { top: 628px; }
  .grown { top: 638px; }
  .record {
    left: 31px; top: 719px; width: 258px; height: 94px; border-radius: 12px;
    background: linear-gradient(90deg, #f4f4f4, var(--note-bg));
    padding: 6px 14px; font-family: "Roboto Condensed", sans-serif;
    font-size: 14px; line-height: 25px; color: var(--note-ink);
  }
</style>
</head>
<body>
<main class="canvas">

  <section class="label label--front" aria-label="Front label">
    <div class="abs brand-vertical">Corrowick Hollow</div>
    <div class="abs pour-line"></div>
    <svg class="abs pour-drop" width="36" height="56" viewBox="0 0 36 56" aria-hidden="true">
      <defs>
        <linearGradient id="dropGold" x1="0" y1="0" x2="1" y2="1">
          <stop offset="0" stop-color="#f0d68a"/>
          <stop offset="0.5" stop-color="#c9a54f"/>
          <stop offset="1" stop-color="#7a5c1c"/>
        </linearGradient>
      </defs>
      <path d="M18 0 C19 18 34 26 34 40 A16 16 0 0 1 2 40 C2 26 17 18 18 0 Z" fill="url(#dropGold)"/>
    </svg>

    <div class="abs brand-circle" aria-hidden="true"></div>
    <div class="abs olive-art" role="img" aria-label="Illustration of a sprig of green olives with leaves"></div>

    <div class="abs front-type extra-virgin">Extra<br>Virgin</div>
    <div class="abs front-type cold-pressed">Cold Pressed</div>
    <div class="abs front-type olive-oil">Olive<br>Oil</div>

    <div class="abs organic">100%<br>organic</div>
    <div class="abs organic-rule"></div>
    <div class="abs front-type volume">500 ML</div>
    <div class="abs front-type origin">Grown and pressed<br>on the Kellaway<br>Peninsula</div>
  </section>

  <section class="label label--back" aria-label="Back label">
    <div class="abs back-circle" aria-hidden="true"></div>
    <div class="abs back-brand">Corrowick Hollow</div>

    <div class="abs nutrition">
      <h2>NUTRITION INFORMATION</h2>
      <table>
        <tr class="head strong"><td>AVG QTY</td><td style="font-weight:400">PER<br>15ML</td><td style="font-weight:400">PER<br>100ML</td></tr>
        <tr><td class="strong">ENERGY (KJ)</td><td>517</td><td>3446</td></tr>
        <tr><td class="strong">PROTEIN (G)</td><td>0</td><td>0</td></tr>
        <tr><td class="strong">FAT (G)</td><td></td><td></td></tr>
        <tr class="sub"><td>- TOTAL</td><td>13.7</td><td>91.5</td></tr>
        <tr class="sub"><td>- SATURATED</td><td>2.1</td><td>14.1</td></tr>
        <tr class="sub"><td>- MONOUNSATURATED</td><td>10.7</td><td>71.5</td></tr>
        <tr class="sub"><td>- POLYUNSATURATED</td><td>0.9</td><td>5.9</td></tr>
        <tr class="sub"><td>- TRANS FATTY ACID</td><td>&lt;0.01</td><td>&lt;0.05</td></tr>
        <tr><td class="strong">CHOLESTERIL (MG)</td><td>0</td><td>0</td></tr>
        <tr><td class="strong">CARBOHYDRATE</td><td>0</td><td>0</td></tr>
        <tr class="sub"><td>- SUGAR (G)</td><td>0</td><td>0</td></tr>
        <tr><td class="strong">OLEIC ACID</td><td>0.1%</td><td></td></tr>
      </table>
    </div>

    <p class="abs back-text ingredients">INGREDIENTS: 100% AUSTRALIAN EXTRA VIRGIN<br>OLIVE OIL COLD PRESSED FRESH</p>
    <p class="abs back-text storage">STORAGE: AIRTIGHT IN COOL DARK PLACE</p>
    <div class="abs rule rule--one"></div>
    <p class="abs back-text made">MADE AND PRODUCED IN AUSTRALIA<br>FROM 100% AUSTRALIAN INGREDIENTS</p>
    <div class="abs rule rule--two"></div>
    <p class="abs back-text grown">GROWN, HARVESTED AND BOTTLED AT<br>THE HOLLOW, PELLANDRY RD.<br>TALLOWMERE. 3847</p>

    <div class="abs record">
      <p>HARVEST DATE:</p>
      <p>BEST BY:</p>
      <p>BATCH:</p>
    </div>
  </section>

</main>
</body>
</html>
```